Diesel Fitting/Mechanical Company Needs a new Business Card

We would like a new business card that showcases our logo and business information.

Industry/Entity Type

Business

Contact Information for Business Card

314 Wendale Street
PO Box 7581 KELBURN RIDGE QLD 4871
Phone: 49312787 Fax: 49312688 Mobile: 0438915276 ABN: 63 519 087 342

Requirements
Must have
• The following email addresses:
• admin@tkservicing.com.au , sales@tkservicing.com.au , accounts@tkservicing.com.au , parts@tkservicing.com.au , office@tkservicing.com.au
• Also need to have the website: www.tkservicing.com.au

```html
<!DOCTYPE html>
<html lang="en">
<head>
<meta charset="utf-8">
<title>TK Servicing – Business Card</title>
<link rel="stylesheet" href="https://fonts.googleapis.com/css2?family=Open+Sans:wght@400;600&family=PT+Sans+Narrow:wght@700&display=swap">
<style>
  :root {
    --page-bg: #a9a8ad;
    --card-black: #1c1c1e;
    --card-black-soft: #3a3a3d;
    --card-white: #f4f5f4;
    --brand-orange: #f0833a;
    --brand-orange-deep: #e8631e;
    --ink: #2f2f31;
    --ink-soft: #4a4a4d;
    --rule: #d9a27a;
  }
  * { box-sizing: border-box; margin: 0; padding: 0; }
  html, body { width: 1200px; height: 863px; overflow: hidden; }
  body {
    background: var(--page-bg);
    font-family: "Open Sans", Arial, sans-serif;
    display: flex;
    flex-direction: column;
    align-items: center;
    justify-content: center;
    gap: 40px;
  }
  .card {
    width: 660px;
    height: 377px;
    position: relative;
    overflow: hidden;
    box-shadow: 0 10px 24px rgba(0,0,0,.25);
  }

  /* Front */
  .card--front {
    background: linear-gradient(115deg, var(--card-black) 0%, var(--card-black-soft) 45%, var(--card-black) 60%, #2a2a2c 100%);
    display: flex;
    align-items: center;
    justify-content: center;
  }
  .brand {
    display: flex;
    align-items: center;
    gap: 14px;
    color: var(--brand-orange);
    font-weight: 600;
  }
  .brand__dot {
    width: 22px; height: 22px;
    border-radius: 50%;
    background: var(--brand-orange);
    flex: none;
  }
  .card--front .brand__name { font-size: 46px; letter-spacing: .5px; }

  /* Back */
  .card--back { background: var(--card-white); }
  .card--back::after {
    content: "";
    position: absolute; left: 0; right: 0; bottom: 0;
    height: 10px;
    background: linear-gradient(90deg, var(--brand-orange-deep), var(--brand-orange));
  }
  .card--back .brand {
    position: absolute; left: 34px; top: 52px;
    gap: 10px;
  }
  .card--back .brand__dot { width: 16px; height: 16px; }
  .card--back .brand__name { font-size: 28px; }

  .address {
    position: absolute; left: 34px; top: 232px;
    font-family: "PT Sans Narrow", "Arial Narrow", sans-serif;
    font-weight: 700;
    font-style: normal;
    font-size: 17px;
    line-height: 1.3;
    color: var(--ink);
  }

  .contact {
    position: absolute; left: 372px; top: 100px;
    width: 270px;
    color: var(--ink-soft);
    font-size: 16px;
  }
  .contact__list { list-style: none; }
  .contact__item {
    display: flex; align-items: center; gap: 9px;
    line-height: 23px;
  }
  .contact__icon { width: 13px; height: 13px; flex: none; fill: var(--ink-soft); }
  .contact__rule {
    height: 1px; background: var(--rule);
    margin: 14px 0 12px;
    width: 215px;
  }
  .emails { list-style: none; line-height: 22px; }
</style>
</head>
<body>

  <section class="card card--front" aria-label="Card front">
    <div class="brand">
      <span class="brand__dot"></span>
      <span class="brand__name">TK Servicing</span>
    </div>
  </section>

  <section class="card card--back" aria-label="Card back">
    <div class="brand">
      <span class="brand__dot"></span>
      <span class="brand__name">TK Servicing</span>
    </div>

    <address class="address">
      314 Wendale Street<br>
      PO Box 7581 KELBURN RIDGE QLD 4871
    </address>

    <div class="contact">
      <ul class="contact__list">
        <li class="contact__item">
          <svg class="contact__icon" viewBox="0 0 16 16"><path d="M4 0h8a1 1 0 0 1 1 1v14a1 1 0 0 1-1 1H4a1 1 0 0 1-1-1V1a1 1 0 0 1 1-1zm1 2v10h6V2zm3 11a1 1 0 1 0 0 2 1 1 0 0 0 0-2z"/></svg>
          49312787
        </li>
        <li class="contact__item">
          <svg class="contact__icon" viewBox="0 0 16 16"><path d="M1 5c0-2 3-3 7-3s7 1 7 3v1.5l-3.5 1V5.5c-1-.5-6-.5-7 0v2L1 6.5zM3 9l2-2h6l2 2v5H3zm5 1a1.8 1.8 0 1 0 0 3.6A1.8 1.8 0 0 0 8 10z"/></svg>
          0438915276
        </li>
        <li class="contact__item">
          <svg class="contact__icon" viewBox="0 0 16 16"><path d="M4 1h7v4H4zM1 6h14v8H1zm2 2v2h3V8zm6 0v1h4V8zm0 2v1h4v-1z"/></svg>
          49312688
        </li>
        <li class="contact__item">
          <svg class="contact__icon" viewBox="0 0 16 16"><path d="M1 3h14v10H1zm1.5 1.5L8 9l5.5-4.5v-.2h-11zM2.5 6.3v5.2h11V6.3L8 10.8z"/></svg>
          office@tkservicing.com.au
        </li>
        <li class="contact__item">
          <svg class="contact__icon" viewBox="0 0 16 16"><path d="M10 1a5 5 0 1 1-3.1 8.9L2.4 14.4 1 13l4.5-4.5A5 5 0 0 1 10 1zm0 2a3 3 0 1 0 0 6 3 3 0 0 0 0-6z"/></svg>
          www.tkservicing.com.au
        </li>
      </ul>
      <div class="contact__rule"></div>
      <ul class="emails">
        <li>admin@tkservicing.com.au</li>
        <li>sales@tkservicing.com.au</li>
        <li>accounts@tkservicing.com.au</li>
        <li>parts@tkservicing.com.au</li>
      </ul>
    </div>
  </section>

</body>
</html>
```